Springboard Quest

I need a design for and advertisement on a Screen at a Doctor's Surgery. The ad would be up for 15 seconds then on a rotation which last 10 minutes. So every 10 minutes if you are sitting in the Doctor's waiting room you will see my ad for 15 seconds.

I am a Personal Trainer and my company is TrueForm Studio. I need this advertisement for my January promotion, I will be running the ad in December. So I need the ad to send to the agent by this Friday.

I attach something for you to start with, basically person sitting in the doctor's waiting room must see headline, value of offer discounted price and webpage. The rest of the stuff should be on ad for those sitting in the waiting room for a long time.

This is a really important ad as January is the biggest month for Personal Trainers, I can't mess this up
Updates

Reason: So I've decided it makes sense to split the project into two, one for the screen, and then the full ad as you have it to fit on an A6 post card. So here are some update: Phone number should be written as (07700) 900482 Change spelling of Program to Programme (£600 Value) change to (Value £600) (£25) Value change to (Value £25) (£45 Value) change to (Value £45) For the screen replace the woman with my picture Also I just got this width to height ratio of the screen is 16:9 The important things to call out on the screen "Early Bird Offer Custom Kick Start Program" "Who Wants To Lose 15 Pounds and Be Healthy in 2015" The Cost of £200 The Savings of £470 The Expiration Date Limited to Fist 10 Individuals Enroll Now The screen should also tell people to pick up a flyer in the Waiting Room Then the flyer, remember just A6 post card should have the full Ad Thank you for taking the time to design my ad

Use colors in my logo. Important for the screen: So I've decided it makes sense to split the project into two, one for the screen, and then the full ad as you have it to fit on an A6 post card. So here are some update: Phone number should be written as (07700) 900482 Change spelling of Program to Programme (£600 Value) change to (Value £600) (£25) Value change to (Value £25) (£45 Value) change to (Value £45) For the screen replace the woman with my picture Also I just got this width to height ratio of the screen is 16:9 The important things to call out on the screen "Early Bird Offer Custom Kick Start Program" "Who Wants To Lose 15 Pounds and Be Healthy in 2015" Cost of £200 Savings of £470 The Expiration Date Limited to First 10 Individuals Enroll Now The screen should also tell people to pick up a flyer in the Waiting Room Then the flyer, remember just A6 post card should have the full Ad Thank you for taking the time to design my ad

Target Market(s)

Women in the age group of 25 to 60, who want to get strong and fit, but are afraid of the weight room. So measure about strength must be subtle or just not there at all. This is not a call for bodybuilders

Industry/Entity Type

Doctor

Requirements
Must have
• Use colors in my logo. Important for the screen:

So I've decided it makes sense to split the project into two, one for the screen, and then the full ad as you have it to fit on an A6 post card.

So here are some update:

Phone number should be written as (07700) 900482
Change spelling of Program to Programme
(£600 Value) change to (Value £600)
(£25) Value change to (Value £25)
(£45 Value) change to (Value £45)
For the screen replace the woman with my picture

Also I just got this width to height ratio of the screen is 16:9

The important things to call out on the screen
"Early Bird Offer Custom Kick Start Program"
"Who Wants To Lose 15 Pounds and Be Healthy in 2015"
The Cost of £200
The Savings of £470
The Expiration Date
Limited to Fist 10 Individuals
Enroll Now

The screen should also tell people to pick up a flyer in the Waiting Room

Then the flyer, remember just A6 post card should have the full Ad

Thank you for taking the time to design my ad

```html
<!DOCTYPE html>
<html lang="en">
<head>
<meta charset="utf-8">
<title>TrueForm Studio – Springboard Quest</title>
<link rel="stylesheet" href="https://fonts.googleapis.com/css2?family=Open+Sans:wght@400;600;700;800&family=Arimo:wght@400;700&display=swap">
<style>
  :root {
    --sky: #1ea4e0;
    --sky-deep: #0e86c6;
    --sky-pale: #8dd6f4;
    --red: #d52b2b;
    --grey: #7a7a7a;
    --ink: #1c1c1c;
    --silver: #c9ccd0;
    --white: #ffffff;
  }
  * { margin: 0; padding: 0; box-sizing: border-box; }
  html, body { width: 1200px; height: 851px; overflow: hidden; background: var(--white); }
  .ad {
    position: relative; width: 1200px; height: 851px; overflow: hidden;
    font-family: "Open Sans", Arial, sans-serif; color: var(--ink); background: var(--white);
  }
  .backdrop { position: absolute; inset: 0; }
  .brand {
    position: absolute; left: 12px; top: 26px; width: 185px; display: flex; align-items: center; gap: 8px;
    font-weight: 800; font-size: 25px; line-height: 1.05; color: var(--sky-deep); letter-spacing: -0.5px;
  }
  .brand-dot { flex: none; width: 16px; height: 16px; border-radius: 50%; background: var(--red); }
  .offer-title {
    position: absolute; left: 206px; top: 38px; white-space: nowrap;
    font-weight: 800; font-size: 21px; line-height: 30px; color: var(--ink);
  }
  .offer-title .big { font-size: 24.5px; }
  .portrait {
    position: absolute; left: 255px; top: 70px; width: 290px; height: 425px;
    background: radial-gradient(ellipse at 50% 28%, #6b4a3a 0 22%, transparent 23%),
                linear-gradient(180deg, #f4f4f4 0%, #f4f4f4 45%, #f26b5e 46%, #ef5f52 100%);
    border-radius: 140px 140px 0 0;
  }
  .price-burst {
    position: absolute; left: 52px; top: 305px; transform: rotate(-12deg); transform-origin: left top;
    font-family: "Open Sans", Arial, sans-serif; font-weight: 800; line-height: 1;
  }
  .price-burst .only { display: block; font-size: 50px; color: var(--sky); padding-left: 16px; }
  .price-burst .amount { display: block; font-size: 72px; color: var(--red); letter-spacing: -1px; }
  .headline {
    position: absolute; left: 568px; top: 84px; font-family: "Arimo", Arial, sans-serif;
    font-weight: 400; letter-spacing: -1px; white-space: nowrap;
  }
  .headline span { display: block; }
  .headline .l1 { font-size: 54px; line-height: 60px; color: var(--sky); }
  .headline .l1 .star { display: inline; color: var(--red); font-size: 38px; vertical-align: top; }
  .headline .l2 { font-size: 54px; line-height: 60px; color: var(--red); }
  .headline .l3 { font-size: 54px; line-height: 60px; color: var(--grey); }
  .headline .l4 { font-size: 108px; line-height: 100px; color: var(--sky); letter-spacing: -3px; }
  .limit {
    position: absolute; left: 568px; top: 366px; font-family: "Arimo", Arial, sans-serif;
    font-size: 20px; color: var(--red); line-height: 1.3;
  }
  .limit .num { font-size: 26px; }
  .limit .enroll { display: block; color: var(--grey); font-size: 25px; }
  .save-tag {
    position: absolute; left: 1010px; top: 40px; width: 210px; transform: rotate(35deg);
    text-align: center; font-weight: 800; color: var(--ink); line-height: 1;
  }
  .save-tag .save { display: block; font-size: 22px; }
  .save-tag .sum { display: block; font-size: 38px; }
  .save-tag .exp { display: block; font-size: 16px; }
  .save-tag .date { display: block; font-size: 38px; }
  .includes { position: absolute; left: 46px; top: 536px; }
  .includes h2 { font-size: 32px; font-weight: 800; line-height: 1.15; }
  .includes h3 { font-size: 20px; font-weight: 700; margin-bottom: 10px; }
  .includes ul { list-style: none; }
  .includes li {
    position: relative; font-size: 16.5px; line-height: 29px; margin-bottom: 6px; width: 390px;
  }
  .includes li strong { font-size: 20px; font-weight: 800; }
  .includes li svg { position: absolute; left: -34px; top: 5px; }
  .contact { position: absolute; left: 568px; top: 526px; }
  .contact .ask { font-size: 28px; color: var(--sky); }
  .contact .phone { font-size: 44px; color: var(--red); line-height: 1.2; }
  .contact .goto { font-size: 20px; color: var(--grey); margin-top: 14px; }
  .contact .url { font-size: 20px; color: var(--sky-deep); line-height: 1.4; margin-top: 4px; }
  .contact .report { font-size: 20px; color: var(--grey); margin-top: 8px; }
  .value-strip {
    position: absolute; left: 0; right: 0; bottom: 4px; text-align: center;
    font-weight: 800; font-size: 28px; color: var(--ink);
  }
  .value-strip .a, .value-strip .deal { color: var(--red); }
  .value-strip .deal { font-size: 30px; }
  .value-strip .was { color: var(--red); text-decoration: line-through; text-decoration-color: var(--ink); }
  .value-strip .small { font-size: 19px; }
  .value-strip .only { color: var(--sky-deep); font-size: 24px; }
</style>
</head>
<body>
<main class="ad">
  <svg class="backdrop" width="1200" height="851" viewBox="0 0 1200 851" aria-hidden="true">
    <defs>
      <linearGradient id="curl" x1="0" y1="0" x2="1" y2="1">
        <stop offset="0" stop-color="#e6f5fd"/>
        <stop offset="0.5" stop-color="#5cc0ec"/>
        <stop offset="1" stop-color="#1ea4e0"/>
      </linearGradient>
      <linearGradient id="wedge" x1="0" y1="0" x2="1" y2="1">
        <stop offset="0" stop-color="#3bb3e9"/>
        <stop offset="1" stop-color="#0e86c6"/>
      </linearGradient>
    </defs>
    <path d="M470 0 C620 25 760 25 900 0 Z" fill="#1ea4e0"/>
    <path d="M960 0 L1200 0 L1200 210 C1120 160 1020 80 960 0 Z" fill="url(#curl)"/>
    <path d="M0 478 C260 462 460 470 720 505 C520 488 260 484 0 500 Z" fill="#c9ccd0"/>
    <path d="M0 496 C250 480 470 486 720 512 L720 851 L0 851 Z" fill="#8dd6f4"/>
    <path d="M600 851 C540 700 560 570 720 500 C900 470 1050 440 1200 420 L1200 851 Z" fill="#ffffff"/>
    <path d="M940 440 L1200 400 L1200 720 Z" fill="url(#wedge)"/>
    <path d="M1010 430 L1200 470 L1200 560 Z" fill="#8dd6f4"/>
    <path d="M0 851 L0 836 C350 798 800 794 1200 818 L1200 851 Z" fill="#ffffff"/>
    <path d="M0 836 C350 798 800 794 1200 818 L1200 812 C800 786 350 790 0 828 Z" fill="#1ea4e0"/>
  </svg>

  <div class="brand"><span class="brand-dot"></span><span>TrueForm<br>Studio</span></div>
  <h1 class="offer-title">EARLY BIRD OFFER CUSTOM <span class="big">KICKSTART PROGRAMME</span></h1>

  <div class="portrait" role="img" aria-label="Photo of the personal trainer smiling, in a coral sports top"></div>

  <div class="price-burst"><span class="only">ONLY</span><span class="amount">£200</span></div>

  <h2 class="headline">
    <span class="l1"><span class="star">*</span>Who wants to</span>
    <span class="l2">lose 15 pounds</span>
    <span class="l3">and be healthy</span>
    <span class="l4">in 2015?</span>
  </h2>
  <p class="limit">Limited to the first <span class="num">10</span> individuals to<span class="enroll">Enroll Now</span></p>

  <div class="save-tag">
    <span class="save">SAVE</span><span class="sum">£470</span><span class="exp">Offer Expires</span><span class="date">31/12/14</span>
  </div>

  <section class="includes">
    <h2>Your KICKSTART</h2>
    <h3>Programme Includes:</h3>
    <ul>
      <li><svg width="14" height="20" viewBox="0 0 14 20"><path d="M2 2 L12 10 L2 18 L5 10 Z" fill="#d52b2b"/></svg>12 Fat-Blasting Training Session with a<br>Personal Trainer <strong>(Value £600)</strong></li>
      <li><svg width="14" height="20" viewBox="0 0 14 20"><path d="M2 2 L12 10 L2 18 L5 10 Z" fill="#d52b2b"/></svg>Exercise Programme Specifically Designed to<br>Meet Your Goals <strong>(Value £25)</strong></li>
      <li><svg width="14" height="20" viewBox="0 0 14 20"><path d="M2 2 L12 10 L2 18 L5 10 Z" fill="#d52b2b"/></svg>Unlimited E-mail Coaching <strong>(Priceless)</strong></li>
      <li><svg width="14" height="20" viewBox="0 0 14 20"><path d="M2 2 L12 10 L2 18 L5 10 Z" fill="#d52b2b"/></svg>Done-For-You Meal Plan <strong>(Value £45)</strong></li>
    </ul>
  </section>

  <section class="contact">
    <p class="ask">Call and Ask for Dana</p>
    <p class="phone">(07700) 900482</p>
    <p class="goto">Or Go To:</p>
    <p class="url">https://trueformstudio.example.net/<br>springboard-programme/</p>
    <p class="report">And get the Sexy Stomach Special Report</p>
  </section>

  <p class="value-strip"><span class="a">A</span> <span class="was">£670</span> <span class="small">Value for</span> <span class="only">ONLY</span> <span class="deal">£200</span></p>
</main>
</body>
</html>
```